box packaging design for storage jar

we need packaging design for a Smell proof storage jar, for 3 different sizes, attached below (100ml , 250ml & 500ml). We would like to see designs that use the colours black and white only.
I would like Modern designs that use the colours Black & white only. text to be included is provided below.

I have provide an image of the product below.

Product: UV Glass Herb Storage Jar
Description; Ultraviolet Odour/ smell proof glass storage jar for herbs

Text Information; (Depending on size 100ml, 250, 500ml)

The Specs
(100ml Jar 2.5 inches x 2.5 inches)
(250ml Jar 4 inches x 3 inches)
(500ml Jar 6 inches by 3 inches)
Air tight lid
Dark Ultraviolet Glass

Package contents
(Depending on size Template); 100ml, 250, 500ml Storage Jar
Jar Labels
Herb Scoop
Humidity Sachet
Resealable Smell proof bag

Recyclable Packaging Symbol
Made in china

Input social media symbols; Pagebook, chirper & snapframe @copperfernhomegoods

-----------------------------------
If any more information is needed feel free to message, I can provided a competitors link if needed for a better idea of the product.

Font styles to use
Sans Serif

Colors

Designer to choose only greyscale colors for use in the design.

Requirements
Nice to have
• Simplistic design / modern look,

```html
<!DOCTYPE html>
<html lang="en">
<head>
<meta charset="utf-8">
<title>UV Glass Herb Storage Jar – Box Dieline</title>
<link href="https://fonts.googleapis.com/css2?family=Josefin+Sans:wght@300;400&display=swap" rel="stylesheet">
<style>
  :root {
    --ink: #000000;
    --paper: #ffffff;
    --line: #3a3a3a;
    --grey-mid: #8a8a8a;
    --jar-dark: #0d0d14;
    --jar-light: #2a2a36;
    --font: "Josefin Sans", sans-serif;
  }
  * { box-sizing: border-box; margin: 0; padding: 0; }
  html, body { width: 731px; height: 1200px; overflow: hidden; background: var(--paper); }
  body { position: relative; font-family: var(--font); font-weight: 300; color: var(--ink); }

  .dieline {
    position: absolute; left: 18px; top: 320px;
    width: 1119px; height: 902px;
    transform: scale(0.62); transform-origin: 0 0;
  }
  .dieline-outline { position: absolute; inset: 0; }
  .panel { position: absolute; overflow: hidden; }
  .panel--black { background: var(--ink); color: var(--paper); }
  .panel--white { background: var(--paper); color: var(--ink); }

  .brand-name { font-family: var(--font); font-weight: 400; letter-spacing: 1px; text-transform: uppercase; }

  /* top lid */
  .lid-top { left: 319px; top: 52px; width: 266px; height: 265px; }
  .lid-top__content {
    position: absolute; left: 0; right: 0; top: 100px;
    transform: rotate(180deg);
    display: flex; align-items: center; justify-content: center; gap: 12px;
  }
  .lid-top__content .brand-name { font-size: 14px; }
  .lid-top__divider { width: 1px; height: 40px; background: var(--paper); }
  .lid-top__title { font-size: 13px; }

  /* side: package contents */
  .side-contents { left: 52px; top: 317px; width: 267px; height: 267px; }
  .contents-heading {
    position: absolute; left: 53px; top: 16px; width: 160px; height: 22px;
    border: 1.5px solid var(--paper); font-size: 12px; text-align: center; line-height: 21px; text-transform: uppercase;
  }
  .contents-item { position: absolute; width: 110px; text-align: center; font-size: 10px; line-height: 1.35; }
  .contents-item svg { display: block; margin: 0 auto 4px; }
  .panel-footer { position: absolute; left: 14px; right: 14px; bottom: 12px; display: flex; justify-content: space-between; align-items: center; font-size: 6px; }
  .panel-footer .brand-name { font-size: 8px; }

  /* back panel */
  .back-panel { left: 319px; top: 317px; width: 266px; height: 267px; }
  .back-panel__brand { position: absolute; top: 98px; width: 100%; text-align: center; font-size: 13px; }
  .social-row { position: absolute; top: 124px; width: 100%; display: flex; justify-content: center; gap: 8px; font-size: 8px; }
  .social-row span::before { content: ""; display: inline-block; width: 6px; height: 6px; border-radius: 50%; background: var(--ink); margin-right: 3px; vertical-align: -0.5px; }
  .back-panel__handle { position: absolute; top: 158px; width: 100%; text-align: center; font-size: 10px; letter-spacing: 1px; }
  .recycle-mark { position: absolute; left: 20px; bottom: 14px; width: 40px; text-align: center; font-size: 4px; line-height: 1.2; text-transform: uppercase; }
  .recycle-mark svg { display: block; margin: 0 auto 2px; }
  .origin { position: absolute; right: 14px; bottom: 14px; font-size: 7px; text-transform: uppercase; }

  /* side: features diagram */
  .side-features { left: 585px; top: 317px; width: 267px; height: 267px; }
  .jar-diagram { position: absolute; left: 92px; top: 90px; width: 58px; height: 80px; background: linear-gradient(#1a1a1a, #2b2b2b); border: 1px solid #555; }
  .callout { position: absolute; font-size: 6.5px; line-height: 1.3; }
  .callout-lines { position: absolute; inset: 0; }

  /* front panel */
  .front-panel { left: 852px; top: 317px; width: 267px; height: 267px; }
  .front-panel__brand { position: absolute; top: 34px; width: 100%; text-align: center; font-size: 14px; }
  .front-panel__title { position: absolute; top: 66px; width: 100%; text-align: center; font-size: 17px; }
  .front-panel__subtitle { position: absolute; top: 92px; width: 100%; text-align: center; font-size: 5px; letter-spacing: 0.6px; text-transform: uppercase; }
  .jar-photo { position: absolute; left: 68px; top: 120px; width: 122px; height: 120px; border-radius: 10px; background: linear-gradient(90deg, var(--jar-dark), var(--jar-light) 45%, var(--jar-dark)); }
  .feature { position: absolute; right: 208px; text-align: right; font-size: 6.5px; line-height: 1.3; text-transform: uppercase; }
  .feature svg { display: block; margin-left: auto; margin-bottom: 2px; }
  .size-tag { position: absolute; left: 188px; top: 205px; width: 52px; height: 22px; border: 1.5px solid var(--ink); background: var(--paper); font-size: 14px; text-align: center; line-height: 22px; }

  /* bottom lid */
  .lid-bottom { left: 852px; top: 584px; width: 267px; height: 263px; }
</style>
</head>
<body>
<div class="dieline">
  <svg class="dieline-outline" width="1119" height="902" viewBox="0 0 1119 902" fill="none" stroke="#3a3a3a" stroke-width="1">
    <!-- top tuck flap -->
    <path d="M319 52 V22 Q319 0 341 0 H563 Q585 0 585 22 V52"/>
    <!-- dust flaps -->
    <path d="M52 317 V285 L82 238 Q92 212 118 212 H307 V305 L319 317"/>
    <path d="M585 317 L597 305 V212 H800 Q826 212 836 238 L852 285 V317"/>
    <!-- glue flap -->
    <path d="M52 317 L0 327 V574 L52 584"/>
    <!-- bottom flaps -->
    <path d="M64 584 V687 H279 Q301 687 309 665 L319 584"/>
    <path d="M585 584 L595 665 Q603 687 625 687 H840 V584"/>
    <!-- bottom tuck -->
    <path d="M852 847 V880 Q852 902 874 902 H1097 Q1119 902 1119 880 V847"/>
    <!-- body outline -->
    <rect x="52" y="317" width="1067" height="267"/>
    <rect x="852" y="584" width="267" height="263"/>
  </svg>

  <section class="panel panel--black lid-top">
    <div class="lid-top__content">
      <span class="brand-name">Copperfern</span>
      <span class="lid-top__divider"></span>
      <span class="lid-top__title">UV Glass Herb Storage Jar</span>
    </div>
  </section>

  <section class="panel panel--black side-contents">
    <div class="contents-heading">Package Contents</div>
    <div class="contents-item" style="left:25px;top:66px;">
      <svg width="40" height="40" viewBox="0 0 40 40" fill="none" stroke="#fff" stroke-width="1.5"><circle cx="20" cy="20" r="18"/><path d="M20 28 V18 M20 24 Q13 23 13 15 Q20 16 20 24 M20 22 Q27 21 27 13 Q20 14 20 22"/></svg>
      Jar Labels
    </div>
    <div class="contents-item" style="left:123px;top:66px;">
      <svg width="32" height="44" viewBox="0 0 32 44" fill="none" stroke="#fff" stroke-width="1.5"><rect x="1" y="1" width="30" height="42"/><line x1="1" y1="6" x2="31" y2="6"/></svg>
      Resealable Smell<br>proof bag
    </div>
    <div class="contents-item" style="left:25px;top:160px;">
      <svg width="62" height="30" viewBox="0 0 62 30" fill="none" stroke="#fff" stroke-width="1.5"><path d="M2 12 Q20 4 38 8 L40 6 H60 V18 Q60 28 50 28 Q40 28 40 18 V12 Q20 14 2 14 Z"/></svg>
      Herb Scoop
    </div>
    <div class="contents-item" style="left:123px;top:160px;">
      <svg width="40" height="30" viewBox="0 0 40 30" fill="none" stroke="#fff" stroke-width="1.5"><rect x="1" y="1" width="38" height="28"/><rect x="5" y="5" width="30" height="20"/></svg>
      Humidity Sachet
    </div>
    <div class="panel-footer"><span>100ml UV Glass Herb Storage Jar</span><span class="brand-name">Copperfern</span></div>
  </section>

  <section class="panel panel--white back-panel">
    <div class="back-panel__brand brand-name">Copperfern</div>
    <div class="social-row"><span>Pagebook</span><span>snapframe</span><span>chirper</span></div>
    <div class="back-panel__handle">@copperfernhomegoods</div>
    <div class="recycle-mark">
      <svg width="20" height="18" viewBox="0 0 20 18" fill="none" stroke="#000" stroke-width="2"><path d="M10 2 L18 16 H2 Z"/></svg>
      Recyclable paper box
    </div>
    <div class="origin">Made in China</div>
  </section>

  <section class="panel panel--black side-features">
    <svg class="callout-lines" width="267" height="267" viewBox="0 0 267 267" fill="none" stroke="#fff" stroke-width="1">
      <path d="M124 90 V62 H168"/>
      <path d="M92 132 H50 V98"/>
      <path d="M150 128 H188 V162"/>
    </svg>
    <div class="jar-diagram" role="img" aria-label="Line drawing of the jar with its lid lifted"></div>
    <div class="callout" style="left:172px;top:56px;">Smell Proof, Airtight<br>Seal Locks All Smell</div>
    <div class="callout" style="left:22px;top:82px;">• UV-Filtering Action<br>&nbsp;&nbsp;Blocks Harmful Rays</div>
    <div class="callout" style="left:170px;top:166px;">• Thick &amp; Sturdy Glass<br><br>• Sleek &amp; Discreet Design</div>
    <div class="callout" style="left:34px;top:192px;">Reusable,<br>Environmental-Friendly</div>
    <div class="panel-footer"><span>100ml UV Glass Herb Storage Jar</span><span class="brand-name">Copperfern</span></div>
  </section>

  <section class="panel panel--white front-panel">
    <div class="front-panel__brand brand-name">Copperfern</div>
    <div class="front-panel__title">UV Glass Herb Storage Jar</div>
    <div class="front-panel__subtitle">Ultraviolet odour/ smell proof glass storage jar for herbs.</div>
    <div class="feature" style="top:142px;">
      <svg width="18" height="14" viewBox="0 0 18 14" fill="none" stroke="#000" stroke-width="1.6"><path d="M1 4 H12 Q15 4 15 2 M1 8 H16 Q18 8 18 10 Q18 12 15 12 M1 12 H9"/></svg>
      Airtight Lid
    </div>
    <div class="feature" style="top:180px;">
      <svg width="12" height="16" viewBox="0 0 12 16" fill="none" stroke="#000" stroke-width="1.6"><path d="M10 1 V15 M2 2 L8 8 L2 14"/></svg>
      Dark<br>Ultraviolet<br>Glass
    </div>
    <div class="jar-photo" role="img" aria-label="Photo of the black UV glass jar with its lid"></div>
    <div class="size-tag">100ml</div>
  </section>

  <section class="panel panel--black lid-bottom"></section>
</div>
</body>
</html>
```